I need a business card design for a new dance business. I offer classical Indian dance tuition and also professional performances. I want to offer the community a variety of Indian dance experiences which include: group class and private tuition, school and preschool educational courses and workshops. dance theatre performances, community function workshops and performances, Kids Bollywood parties, wedding & conference performances, mouth percussion classes, Indian mythology/ dance costume and make up workshops.
The final design should communicate a feeling and impression of the vibrance and energy of Indian dance.
Updates
Hi Everyone,
Project Deadline Extended
Reason: I would like to refine a few changes to the details of this lovely design and we have run out of time!
Project Deadline Extended
Reason: Still waiting to hear back form designer re two possible changes to the card design. Tomorrow is the deadline and I have sent several messages but with no response. I need to see this through before selecting this lovely design.
Thank you.
Tara
Industry/Entity Type
Preschool
Requirements
Must have
- The front of the business card should have the photo of me (my face and torso), surrounded entirely by a border of bright magenta (to match the magenta of my lipstick - it is the same as the magenta on my skirt in the second photo). Within the top border I want (perhaps yellow-gold) writing to say "Tara Holloway - Artistic Director" and within the bottom border it should read "Silver Creek Kathak Studio." If you turn the card on its side the left border should have my telephone number: 0417 826 394 and the right-hand border should read: silvercreekkathakstudio@fernmail.example
The reverse of the card should be the orange of the dance costume
and I'd like the picture of my feet and legs to be on the right side of the back of the card as a side border. Centre-aligned on the orange background it should read (perhaps in dark magenta):
Indian dance classes + private tuition
School + preschool educational courses and workshops
Dance theatre performances
Community function workshops and performances
Children's Bollywood parties
Wedding + conference performances
Mouth percussion classes
Indian mythology and dance demonstration workshops
Dance costume and make-up workshops
Nice to have
- A lovely artistic but easy-to-read font would be nice.

```html
<!DOCTYPE html>
<html lang="en">
<head>
<meta charset="utf-8">
<title>Silver Creek Kathak Studio – Business Card</title>
<link rel="stylesheet" href="https://fonts.googleapis.com/css2?family=Great+Vibes&family=Parisienne&family=Marcellus&display=swap">
<style>
  :root {
    --page: #ffffff;
    --magenta: #b01a8c;
    --magenta-deep: #9a1478;
    --orange: #e8761c;
    --orange-deep: #d8620f;
    --gold: #f3c94a;
    --gold-soft: #f6d77a;
    --ink: #1a1014;
    --plum: #5a0f3a;
  }
  * { margin: 0; padding: 0; box-sizing: border-box; }
  html, body {
    width: 1200px; height: 900px; overflow: hidden;
    background: var(--page);
  }
  .canvas { position: relative; width: 1200px; height: 900px; }

  .card {
    position: absolute; left: 310px; width: 590px; overflow: hidden;
    box-shadow: 4px 6px 10px rgba(0,0,0,0.18);
  }

  /* Front */
  .card--front {
    top: 40px; height: 390px;
    background: linear-gradient(135deg, var(--magenta) 0%, var(--magenta-deep) 100%);
  }
  .portrait {
    position: absolute; left: 90px; top: 16px; width: 360px; height: 344px;
    background: radial-gradient(ellipse at 50% 45%, #e9a24a 0%, #c86a2c 40%, rgba(176,26,140,0) 75%);
  }
  .front-band {
    position: absolute; left: 0; bottom: 0; width: 100%; height: 30px;
    background: linear-gradient(180deg, var(--orange) 0%, var(--orange-deep) 100%);
  }
  .phone {
    position: absolute; left: 12px; top: 26px;
    writing-mode: vertical-rl;
    font-family: "Marcellus", serif; font-size: 34px; letter-spacing: 4px;
    color: var(--gold);
  }
  .email {
    position: absolute; right: 10px; top: 20px;
    writing-mode: vertical-rl;
    font-family: "Marcellus", serif; font-size: 14px;
    color: var(--gold);
  }
  .name {
    position: absolute; left: 95px; top: 226px;
    font-family: "Great Vibes", cursive; font-size: 76px; line-height: 1;
    color: var(--ink);
  }
  .title {
    position: absolute; left: 375px; top: 300px;
    font-family: "Parisienne", cursive; font-size: 20px;
    color: var(--gold-soft);
  }
  .studio--front {
    position: absolute; left: 40px; top: 322px;
    font-family: "Parisienne", cursive; font-size: 30px;
    color: var(--gold);
  }

  /* Back */
  .card--back {
    top: 456px; height: 368px;
    background: linear-gradient(135deg, var(--orange) 0%, var(--orange-deep) 100%);
  }
  .services {
    position: absolute; left: 0; top: 46px; width: 440px;
    list-style: none; text-align: center;
    font-family: "Marcellus", serif; font-size: 14.5px; line-height: 25px;
    color: var(--plum);
  }
  .feet-photo {
    position: absolute; right: 0; top: 0; width: 146px; height: 100%;
    background: linear-gradient(180deg, #3a1030 0%, #8c1a72 35%, #c2581c 65%, #6a3a2a 100%);
  }
  .studio--back {
    position: absolute; left: 36px; top: 300px;
    font-family: "Parisienne", cursive; font-size: 30px;
    color: var(--gold-soft);
  }
</style>
</head>
<body>
<main class="canvas">
  <section class="card card--front" aria-label="Business card front">
    <div class="portrait" role="img" aria-label="Photograph of Tara in classical Indian dance costume and jewellery, face and torso"></div>
    <div class="front-band" role="img" aria-label="Orange patterned band"></div>
    <p class="phone">0417 826 394</p>
    <p class="email">silvercreekkathakstudio@fernmail.example</p>
    <h1 class="name">Tara Holloway</h1>
    <p class="title">Artistic Director</p>
    <p class="studio studio--front">Silver Creek Kathak Studio</p>
  </section>

  <section class="card card--back" aria-label="Business card back">
    <ul class="services">
      <li>Indian dance classes + private tuition</li>
      <li>School + preschool educational courses and workshops</li>
      <li>Dance theatre performances</li>
      <li>Community function workshops and performances</li>
      <li>Children's Bollywood parties</li>
      <li>Wedding + conference performances</li>
      <li>Mouth percussion classes</li>
      <li>Indian mythology and dance demonstration workshops</li>
      <li>Dance costume and make-up workshops</li>
    </ul>
    <div class="feet-photo" role="img" aria-label="Photograph of dancer's legs and feet in magenta and gold costume"></div>
    <p class="studio studio--back">Silver Creek Kathak Studio</p>
  </section>
</main>
</body>
</html>
```